Hot Life Science Consulting firm flyer design

We need to a flyer design for a consulting firm called Valtrix. We provide FDA compliance expertise for the Medical Device, Pharmaceutical, and Biotech Industries. The final design should communicate a sense of professionalism and integrity.

Target Market(s)

Medical Device, Pharmaceutical, and Biotech companies

Industry/Entity Type

Management Consulting

Colors
0255a3
3176b5
85abd2
cedeed
eaf1f7
ffffff

Requirements
Must have
• Use the attached PPT to create a sense of flow from the different areas of service we provide.
Nice to have
• 3 fold design with a front page with our logo and tag line: "Experts in compliance for the Medical Device, Pharmaceutical, and Biotech Industries"

```html
<!DOCTYPE html>
<html lang="en">
<head>
<meta charset="utf-8">
<title>Valtrix Tri-fold Brochure</title>
<link rel="stylesheet" href="https://fonts.googleapis.com/css2?family=Open+Sans:wght@400;600;700&display=swap">
<style>
:root{
  --navy:#0255a3;
  --blue:#3176b5;
  --sky:#85abd2;
  --mist:#cedeed;
  --ice:#eaf1f7;
  --white:#ffffff;
  --stage:#dde6ef;
  --ink:#1d3b5e;
}
*{box-sizing:border-box;margin:0;padding:0}
html,body{width:750px;height:1200px;overflow:hidden}
body{background:var(--stage);font-family:"Open Sans",Arial,sans-serif;position:relative;color:var(--white)}
.sheet{position:absolute;left:20px;width:710px;height:560px;display:grid;grid-template-columns:repeat(3,1fr);box-shadow:0 4px 14px rgba(2,40,90,.18)}
.sheet--outside{top:25px}
.sheet--inside{top:615px}
.panel{position:relative;overflow:hidden;padding:22px 16px 16px}
.panel--deep{background:linear-gradient(160deg,var(--navy) 0%,var(--blue) 70%,var(--navy) 100%)}
.panel--bright{background:linear-gradient(180deg,var(--blue) 0%,var(--navy) 100%)}
.panel--light{background:var(--white);color:var(--ink)}
.panel--fade{background:linear-gradient(180deg,var(--navy) 0%,var(--blue) 55%,var(--sky) 100%)}
.panel-title{font-size:17px;font-weight:700;line-height:1.1;margin-bottom:6px}
.panel-lead{font-size:8px;font-weight:600;line-height:1.35;margin-bottom:8px;color:var(--mist)}
.service-list{list-style:none;font-size:7.4px;line-height:1.38}
.service-list li{padding-left:8px;position:relative}
.service-list li::before{content:"";position:absolute;left:0;top:4px;width:3px;height:3px;background:var(--white);border-radius:50%}
.service-list .sub{padding-left:18px}
.service-list .sub::before{left:10px;background:var(--sky)}
.service-list .gap{margin-top:5px}
.web{position:absolute;bottom:12px;left:0;right:0;text-align:center;font-size:7px;letter-spacing:2px;font-weight:600}
.brand{display:flex;align-items:center;gap:6px;font-weight:700;font-size:22px;letter-spacing:.5px}
.brand-dot{width:12px;height:12px;border-radius:50%;background:var(--sky)}
.photo{position:absolute;background:linear-gradient(135deg,var(--mist),var(--sky) 50%,var(--blue))}
/* outside middle */
.cover-photo{top:0;left:0;right:0;height:230px;clip-path:polygon(0 0,100% 0,100% 75%,0 100%)}
.cover-copy{position:absolute;top:250px;left:0;right:0;text-align:center;font-size:7.5px;line-height:1.5;padding:0 34px;color:var(--ice)}
.cover-brand{position:absolute;top:345px;left:0;right:0;display:flex;flex-direction:column;align-items:center;gap:6px}
.cover-brand .brand{color:var(--white)}
.cover-brand p{font-size:7px;text-align:center;line-height:1.4;padding:0 40px;color:var(--mist)}
/* outside right */
.front-brand{position:absolute;top:48px;left:0;right:0;display:flex;justify-content:center}
.front-brand .brand{color:var(--navy)}
.front-tag{position:absolute;top:84px;left:20px;right:20px;text-align:center;font-size:7.5px;color:var(--blue);line-height:1.4}
.orb{border-radius:50%;border:4px solid var(--white);box-shadow:0 2px 6px rgba(2,40,90,.3)}
.orb--main{top:190px;left:50px;width:170px;height:170px}
.orb--a{top:140px;left:22px;width:80px;height:80px;background:linear-gradient(135deg,var(--ice),var(--sky))}
.orb--b{top:330px;left:20px;width:70px;height:70px;background:linear-gradient(135deg,var(--sky),var(--navy))}
.front-band{position:absolute;left:0;right:0;bottom:0;height:150px;background:linear-gradient(180deg,var(--blue),var(--navy));clip-path:polygon(0 40%,100% 0,100% 100%,0 100%)}
.front-band + .web{color:var(--white)}
/* inside right */
.lab-photo{left:0;right:0;bottom:0;height:140px;background:linear-gradient(180deg,var(--sky),var(--ice) 40%,var(--blue))}
</style>
</head>
<body>

<section class="sheet sheet--outside">
  <div class="panel panel--deep">
    <h2 class="panel-title">Managed Solutions</h2>
    <p class="panel-lead">Optimization of Resources to Lead and Execute Your Initiatives</p>
    <ul class="service-list">
      <li>Investigation and Backlog Management</li>
      <li>Complaint and Nonconformance Action/CAPA System Design &amp; Execution</li>
      <li>Document Management &amp; Optimization</li>
      <li class="sub">Records Design Management</li>
      <li class="sub">Review, including Batch Records and Design History Records</li>
      <li class="gap">Technical Writing</li>
      <li>Validation Planning and Execution</li>
      <li class="sub">Computer Systems</li>
      <li class="sub">Process</li>
      <li class="sub">Cleaning</li>
      <li class="sub">Equipment</li>
      <li class="gap">Material and Product Investigation Activities</li>
      <li class="sub">Sampling &amp; Inspection</li>
      <li class="sub">Incoming Materials</li>
      <li class="sub">Finished Goods</li>
      <li class="gap">Post Market Surveillance and Complaint Management</li>
      <li>Quality System Design and Optimization</li>
      <li>Annual Product Reviews</li>
      <li>Training</li>
      <li>Investigation Workstream Management</li>
      <li>Technology Transfer</li>
      <li>Audit Management</li>
    </ul>
    <p class="web">WWW.VALTRIX-CONSULT.COM</p>
  </div>

  <div class="panel panel--bright">
    <div class="photo cover-photo" role="img" aria-label="Laboratory scientist and medical device collage"></div>
    <p class="cover-copy">Trusted compliance partners for regulated industries. We help teams prepare, remediate and sustain quality systems with clarity and care.</p>
    <div class="cover-brand">
      <div class="brand"><span class="brand-dot"></span>Valtrix</div>
      <p>Guidance that keeps your products safe, your records sound and your teams ready.</p>
    </div>
    <p class="web">WWW.VALTRIX-CONSULT.COM</p>
  </div>

  <div class="panel panel--light">
    <div class="front-brand"><div class="brand"><span class="brand-dot"></span>Valtrix</div></div>
    <p class="front-tag">Experts in compliance for the Medical Device, Pharmaceutical, and Biotech Industries</p>
    <div class="photo orb orb--a" role="img" aria-label="Laboratory glassware close-up"></div>
    <div class="photo orb orb--main" role="img" aria-label="Medical device on a clinical workspace"></div>
    <div class="photo orb orb--b" role="img" aria-label="Researcher working with samples"></div>
    <div class="front-band"></div>
    <p class="web">WWW.VALTRIX-CONSULT.COM</p>
  </div>
</section>

<section class="sheet sheet--inside">
  <div class="panel panel--deep">
    <h2 class="panel-title">Strategic Services</h2>
    <p class="panel-lead">Providing Guidance and Direction to Your Operational Excellence</p>
    <ul class="service-list">
      <li>Due Diligence – Regulation and Integration Support</li>
      <li>FDA Compliance and Remediation – Warning Letters, Consent Decrees and 483 Responses</li>
      <li>Post Market Surveillance Strategy</li>
      <li>FDA Mock Inspections</li>
      <li>FDA Inspection Readiness, Preparation and Review</li>
      <li>Information Technology System Design, Integration and Validation</li>
      <li>Interim Leadership Roles</li>
      <li class="gap">Manufacturing Process Improvement and Optimization</li>
      <li>Product Platform Optimization</li>
      <li>Project and Program Management</li>
      <li>Quality &amp; Regulatory Assessments and Audits</li>
      <li>Quality Management, Management Commitment and Responsibility</li>
      <li>Supplier Quality Programs</li>
      <li>Training Initiatives and Mentoring</li>
    </ul>
  </div>

  <div class="panel panel--bright">
    <h2 class="panel-title">Resource Solutions</h2>
    <p class="panel-lead">Immediate Augmentation at Your Organization Across</p>
    <ul class="service-list">
      <li>Auditors</li>
      <li>Batch Record Reviews</li>
      <li>CAPA Investigators</li>
      <li>Change Control Specialists</li>
      <li>Complaint System Architects</li>
      <li>Document Control Specialists</li>
      <li>Distribution Center Personnel</li>
      <li>Engineers</li>
      <li class="sub">Automation</li>
      <li class="sub">Biomedical</li>
      <li class="sub">Electrical</li>
      <li class="sub">Mechanical</li>
      <li class="sub">Process</li>
      <li class="sub">Quality</li>
      <li class="sub">Validation</li>
      <li class="sub">Manufacturing &amp; Industrial</li>
      <li>Packaging</li>
      <li>Project Engineers</li>
      <li>Regulatory Associates</li>
      <li>Quality Assurance</li>
      <li>Product Surveillance Leads</li>
      <li>Complaint Management</li>
      <li>QC Lab Chemists</li>
      <li>QC Lab Microbiology</li>
    </ul>
  </div>

  <div class="panel panel--fade">
    <ul class="service-list">
      <li>Laboratory and Software Quality Leads</li>
      <li>Regulatory Affairs Professionals</li>
      <li>Software Quality Assurance and Testing Specialists</li>
      <li>Medical Writers</li>
      <li>Sterility Assurance Professionals</li>
      <li>Supplier Quality Engineers</li>
      <li>Training Professionals</li>
      <li>Validation</li>
      <li class="sub">Cleaning</li>
      <li class="sub">Computerized Systems</li>
      <li class="sub">Facilities and Utilities</li>
      <li class="sub">Manufacturing Equipment</li>
      <li class="sub">Process</li>
      <li class="sub">Laboratory</li>
      <li class="sub">Test Methods</li>
      <li class="sub">Controlled Environments</li>
    </ul>
    <div class="photo lab-photo" role="img" aria-label="Test tubes in a laboratory rack"></div>
  </div>
</section>

</body>
</html>
```